Halvex Consulting

Hi,
I have my own network consulting business (just me)
and need to get a logo and business card design together,

Based in New Zealand,

Gareth Pollard
Unified Communications and Network Architect

/design engineer,
and would like this to be the basis for personal branding and company identity

Reason: I will be off site for a couple of days - so you have some more time

Business

• I have the basis for a optional logo - needs color -

```html
<!DOCTYPE html>
<html lang="en">
<head>
<meta charset="utf-8">
<title>Halvex Consulting – Business Cards</title>
<link rel="stylesheet" href="https://fonts.googleapis.com/css2?family=Exo+2:ital,wght@0,400;1,700&display=swap">
<style>
  :root {
    --page: #ffffff;
    --ice-light: #f4ffff;
    --ice: #c9fbfc;
    --cyan: #00ccff;
    --cyan-soft: #a9f3f8;
    --brand-blue: #1aa3e6;
    --grey-light: #f6f6f6;
    --grey: #e2e2e2;
    --ink: #111111;
    --white: #ffffff;
  }
  * { box-sizing: border-box; margin: 0; padding: 0; }
  html, body { width: 1200px; height: 960px; overflow: hidden; background: var(--page); }
  body { position: relative; font-family: "Exo 2", sans-serif; }

  .card {
    position: absolute;
    width: 543px;
    height: 309px;
    border-radius: 32px;
    overflow: hidden;
  }
  .card--ice { background: radial-gradient(ellipse at 50% 50%, var(--ice-light) 0%, var(--ice) 100%); }
  .card--grey { background: radial-gradient(ellipse at 30% 40%, var(--grey-light) 0%, var(--grey) 100%); }

  .front-ice { left: 45px; top: 156px; }
  .front-dark { left: 622px; top: 156px; }
  .back-ice { left: 45px; top: 495px; }
  .back-dark { left: 622px; top: 495px; }

  .card__art { position: absolute; inset: 0; width: 100%; height: 100%; }

  .brand-dot {
    position: absolute;
    border-radius: 50%;
    background: radial-gradient(circle at 40% 35%, #bff9ff 0%, #4fe0f5 100%);
  }
  .brand-name {
    position: absolute;
    font-weight: 400;
    color: var(--brand-blue);
    white-space: nowrap;
    letter-spacing: 0.3px;
  }

  .person {
    position: absolute;
    text-align: center;
    transform: translateX(-50%);
    white-space: nowrap;
  }
  .person__name {
    display: inline-block;
    font-size: 21px;
    font-style: italic;
    font-weight: 700;
    letter-spacing: 0.8px;
    padding: 0 10px 1px;
    border-bottom: 2px solid var(--cyan);
    line-height: 1.1;
  }
  .person__title {
    margin-top: 3px;
    font-size: 8.5px;
    font-style: italic;
    font-weight: 700;
    letter-spacing: 0.3px;
  }
  .person--dark { color: var(--ink); }
  .person--light { color: var(--white); }

  .accent-bar {
    position: absolute;
    left: 0; top: 270px;
    width: 325px; height: 9px;
    background: var(--cyan);
  }
  .halo {
    position: absolute;
    left: 381px; top: 63px;
    width: 132px; height: 132px;
    border-radius: 50%;
    background: radial-gradient(circle at 45% 40%, #d2fbfd 0%, var(--cyan-soft) 100%);
  }
</style>
</head>
<body>

  <!-- Front, light -->
  <section class="card card--ice front-ice">
    <div class="halo"></div>
    <span class="brand-dot" style="left:70px; top:26px; width:40px; height:40px;"></span>
    <span class="brand-name" style="left:16px; top:83px; font-size:16px;">Halvex Consulting</span>
    <div class="person person--dark" style="left:269px; top:138px;">
      <div class="person__name">Gareth Pollard</div>
      <div class="person__title">Unified Communications and Network Architect</div>
    </div>
    <div class="accent-bar"></div>
  </section>

  <!-- Front, dark -->
  <section class="card card--grey front-dark">
    <svg class="card__art" viewBox="0 0 543 309" preserveAspectRatio="none" aria-hidden="true">
      <defs>
        <radialGradient id="swoop-front" cx="0.95" cy="0.95" r="1.1">
          <stop offset="0" stop-color="#000"/>
          <stop offset="0.5" stop-color="#2a2a2a"/>
          <stop offset="1" stop-color="#8a8a8a"/>
        </radialGradient>
      </defs>
      <path d="M55 309 C150 140 300 55 543 46 L543 309 Z" fill="url(#swoop-front)"/>
    </svg>
    <span class="brand-dot" style="left:66px; top:26px; width:40px; height:40px;"></span>
    <span class="brand-name" style="left:11px; top:87px; font-size:16px;">Halvex Consulting</span>
    <div class="person person--light" style="left:327px; top:180px;">
      <div class="person__name">Gareth Pollard</div>
      <div class="person__title">Unified Communications and Network Architect</div>
    </div>
  </section>

  <!-- Back, light -->
  <section class="card card--ice back-ice">
    <span class="brand-dot" style="left:241px; top:102px; width:62px; height:62px;"></span>
    <span class="brand-name" style="left:50%; top:195px; transform:translateX(-50%); font-size:25px;">Halvex Consulting</span>
  </section>

  <!-- Back, dark -->
  <section class="card card--grey back-dark">
    <svg class="card__art" viewBox="0 0 543 309" preserveAspectRatio="none" aria-hidden="true">
      <defs>
        <radialGradient id="swoop-back" cx="0.1" cy="0.9" r="1.1">
          <stop offset="0" stop-color="#000"/>
          <stop offset="0.5" stop-color="#2a2a2a"/>
          <stop offset="1" stop-color="#8a8a8a"/>
        </radialGradient>
      </defs>
      <path d="M0 46 C250 60 420 150 487 309 L0 309 Z" fill="url(#swoop-back)"/>
    </svg>
    <span class="brand-dot" style="left:432px; top:25px; width:80px; height:80px;"></span>
  </section>

</body>
</html>
```